Carpet Cleaning Door Hanger Design Project

please design a door hanger for us. we do carpet cleaning. our company name is Bright Loom Fibers. our telephone number is 866-430-2715.

please make a special offer coupon.

please add bullets containing the following info-
Professional carpet, hardwood, tile & grout deep steam cleaning.
kid & pet safe.
fast drying.
100% eco friendly / toxin free products.
pet stain/s & odor control.
same day appointments.
clean uniformed employees.
and please put few other catchy lines.

please make a $20.00 of carpet cleaning coupon (restrictions apply).
please make a rooms starting at $59.99 (restrictions apply).

please also put- when you want the best for less call bright loom fibers.

Target Market(s)

home owners, home renters. new home buyers. new home sellers.

Industry/Entity Type

Home Improvement

Requirements
Must have
• special offer.
• double sided.
• must be a design for a door hanger.
Nice to have
• 100% satisfaction guaranteed bubble.
Should not have
• no website please

```html
<!DOCTYPE html>
<html lang="en">
<head>
<meta charset="utf-8">
<title>Bright Loom Fibers – Door Hanger</title>
<link rel="stylesheet" href="https://fonts.googleapis.com/css2?family=Montserrat:ital,wght@0,700;0,800;0,900;1,800;1,900&family=Lato:wght@700;900&display=swap">
<style>
  :root {
    --stage: #3b3b3d;
    --blue-deep: #1f66b1;
    --blue-mid: #3d86c9;
    --blue-light: #8fc0e8;
    --red: #e3202a;
    --red-dark: #b3141c;
    --hole: #fdf6c0;
    --ink: #2f2f2f;
    --gold: #f2c21b;
    --gold-dark: #d79a09;
    --eco: #3aa23a;
    --white: #ffffff;
  }
  html, body {
    margin: 0;
    width: 1094px;
    height: 1200px;
    overflow: hidden;
    background: var(--stage);
  }
  .canvas { position: relative; width: 1094px; height: 1200px; }
  .hanger { position: absolute; top: 98px; width: 432px; height: 1005px; display: block; }
  .hanger--front { left: 102px; }
  .hanger--back { left: 560px; }
  .title { font-family: "Montserrat", sans-serif; font-weight: 800; fill: var(--white); }
  .ribbon-label { font-family: "Montserrat", sans-serif; font-weight: 900; font-style: italic; fill: var(--white); }
  .price { font-family: "Montserrat", sans-serif; font-weight: 900; }
  .fine { font-family: "Montserrat", sans-serif; font-weight: 800; font-style: italic; fill: var(--red); }
  .arc-label { font-family: "Lato", sans-serif; font-weight: 700; fill: var(--red); }
  .bullet { font-family: "Lato", sans-serif; font-weight: 900; fill: var(--ink); font-size: 30px; }
  .coupon-text { font-family: "Montserrat", sans-serif; font-weight: 800; fill: var(--red); }
  .cta { font-family: "Montserrat", sans-serif; font-weight: 900; fill: var(--white); }
  .phone { font-family: "Montserrat", sans-serif; font-weight: 800; fill: var(--ink); }
</style>
</head>
<body>
<main class="canvas">

  <!-- Front side -->
  <svg class="hanger hanger--front" viewBox="0 0 539 1256" xmlns="http://www.w3.org/2000/svg">
    <defs>
      <linearGradient id="front-sky" x1="0" y1="0" x2="0" y2="1">
        <stop offset="0" stop-color="#2c6fb6"/>
        <stop offset="0.55" stop-color="#8fc0e8"/>
        <stop offset="1" stop-color="#2a6ab2"/>
      </linearGradient>
      <linearGradient id="room-photo" x1="0" y1="0" x2="1" y2="1">
        <stop offset="0" stop-color="#6f7478"/>
        <stop offset="0.45" stop-color="#d9d2c4"/>
        <stop offset="1" stop-color="#c9c0b1"/>
      </linearGradient>
      <linearGradient id="carpet-tone" x1="0" y1="0" x2="0" y2="1">
        <stop offset="0" stop-color="#f3f0ea"/>
        <stop offset="1" stop-color="#ddd6ca"/>
      </linearGradient>
      <linearGradient id="price-red" x1="0" y1="0" x2="0" y2="1">
        <stop offset="0" stop-color="#b3141c"/>
        <stop offset="0.55" stop-color="#ea2029"/>
        <stop offset="1" stop-color="#c8161f"/>
      </linearGradient>
      <radialGradient id="eco-disc" cx="0.45" cy="0.4" r="0.6">
        <stop offset="0" stop-color="#9bd86b"/>
        <stop offset="1" stop-color="#2f8f2f"/>
      </radialGradient>
      <path id="eco-arc" d="M 24,815 A 124,124 0 0 1 244,882"/>
    </defs>

    <rect class="carpet-area" width="539" height="1256" fill="url(#carpet-tone)" role="img" aria-label="Close-up of soft white shag carpet"/>

    <path class="room-photo" d="M0 430 H539 V920 Q270 1000 0 935 Z" fill="url(#room-photo)" role="img" aria-label="Technician steam-cleaning a beige carpet in a living room beside an armchair and a potted fern"/>
    <path d="M0 935 Q270 1000 539 920" fill="none" stroke="#2a6ab2" stroke-width="8"/>

    <path class="sky-band" d="M0 0 H539 V440 Q280 540 0 448 Z" fill="url(#front-sky)"/>
    <path d="M0 448 Q280 540 539 440" fill="none" stroke="#111" stroke-width="5"/>

    <line x1="130" y1="0" x2="202" y2="82" stroke="var(--red)" stroke-width="3" stroke-dasharray="10 7"/>
    <circle cx="270" cy="168" r="94" fill="var(--hole)" stroke="var(--red)" stroke-width="2.5" stroke-dasharray="8 5"/>

    <text class="title" x="270" y="372" font-size="82" text-anchor="middle" textLength="470" lengthAdjust="spacingAndGlyphs">BRIGHT LOOM</text>
    <text class="title" x="270" y="448" font-size="82" text-anchor="middle">FIBERS</text>

    <circle class="eco-seal" cx="117" cy="893" r="98" fill="#ffffff" stroke="var(--eco)" stroke-width="6" role="img" aria-label="Eco friendly badge"/>
    <circle cx="117" cy="893" r="72" fill="url(#eco-disc)"/>
    <text class="arc-label" font-size="29"><textPath href="#eco-arc">Toxin Free Products</textPath></text>

    <path class="ribbon" d="M98 990 L464 970 L418 1034 L148 1034 Z" fill="var(--red-dark)"/>
    <text class="ribbon-label" x="275" y="1026" font-size="36" text-anchor="middle">STARTING AT</text>

    <text class="price" x="60" y="1194" font-size="200" fill="url(#price-red)" textLength="350" lengthAdjust="spacingAndGlyphs">$59</text>
    <text class="price" x="414" y="1192" font-size="50" fill="var(--red)">.99</text>
    <text class="fine" x="146" y="1238" font-size="21">(RESTRICTIONS APPLY).</text>
  </svg>

  <!-- Back side -->
  <svg class="hanger hanger--back" viewBox="0 0 539 1256" xmlns="http://www.w3.org/2000/svg">
    <defs>
      <linearGradient id="shag-tone" x1="0" y1="0" x2="1" y2="1">
        <stop offset="0" stop-color="#e7e2d8"/>
        <stop offset="0.5" stop-color="#f4f1eb"/>
        <stop offset="1" stop-color="#d8d1c4"/>
      </linearGradient>
      <linearGradient id="cta-band" x1="0" y1="0" x2="0" y2="1">
        <stop offset="0" stop-color="#1f66b1"/>
        <stop offset="0.7" stop-color="#2a74bd"/>
        <stop offset="1" stop-color="#7fb3e2"/>
      </linearGradient>
      <radialGradient id="gold" cx="0.4" cy="0.35" r="0.7">
        <stop offset="0" stop-color="#fff08a"/>
        <stop offset="0.6" stop-color="#f2c21b"/>
        <stop offset="1" stop-color="#d38f05"/>
      </radialGradient>
    </defs>

    <rect width="539" height="1256" fill="#ffffff"/>

    <path class="shag-photo" d="M0 0 H539 V432 Q300 530 0 432 Z" fill="url(#shag-tone)" role="img" aria-label="Close-up of fluffy white shag carpet"/>
    <path d="M0 432 Q300 530 539 432" fill="none" stroke="#111" stroke-width="5"/>

    <line x1="408" y1="0" x2="336" y2="92" stroke="var(--red)" stroke-width="3" stroke-dasharray="10 7"/>
    <circle cx="268" cy="168" r="94" fill="var(--hole)" stroke="var(--red)" stroke-width="2.5" stroke-dasharray="8 5"/>

    <circle class="guarantee-seal" cx="413" cy="353" r="120" fill="url(#gold)" role="img" aria-label="Satisfaction guarantee seal"/>

    <g class="feature-list">
      <g class="ticks" fill="none" stroke="var(--red)" stroke-width="2.5">
        <circle cx="44" cy="518" r="9"/><path d="M39 518 l4 5 l10 -12"/>
        <circle cx="44" cy="593" r="9"/><path d="M39 593 l4 5 l10 -12"/>
        <circle cx="44" cy="633" r="9"/><path d="M39 633 l4 5 l10 -12"/>
        <circle cx="44" cy="675" r="9"/><path d="M39 675 l4 5 l10 -12"/>
        <circle cx="44" cy="751" r="9"/><path d="M39 751 l4 5 l10 -12"/>
        <circle cx="44" cy="792" r="9"/><path d="M39 792 l4 5 l10 -12"/>
      </g>
      <text class="bullet" x="64" y="528">Professional carpet,hardwood,</text>
      <text class="bullet" x="64" y="563">tile &amp; grout deep steam cleaning.</text>
      <text class="bullet" x="64" y="603">Kid &amp; pet safe.</text>
      <text class="bullet" x="64" y="643">Fast drying.</text>
      <text class="bullet" x="64" y="685">100% eco friendly / toxin</text>
      <text class="bullet" x="64" y="721">free products.</text>
      <text class="bullet" x="64" y="761">Pet stain/s &amp; odor control.</text>
      <text class="bullet" x="64" y="802">Same day appointments.</text>
      <text class="bullet" x="64" y="843">Clean uniformed employees.</text>
    </g>

    <rect class="cta-band" x="0" y="950" width="539" height="306" fill="url(#cta-band)"/>

    <g class="coupon">
      <rect x="40" y="873" width="458" height="152" fill="#ffffff" stroke="#555" stroke-width="2.5" stroke-dasharray="9 6"/>
      <text class="coupon-text" x="66" y="995" font-size="122" textLength="228" lengthAdjust="spacingAndGlyphs">$20</text>
      <text class="coupon-text" x="302" y="940" font-size="25" textLength="168" lengthAdjust="spacingAndGlyphs">OFF CARPET</text>
      <text class="coupon-text" x="302" y="970" font-size="25">CLEANING</text>
      <text class="coupon-text" x="302" y="992" font-size="13">(RESTRICTIONS APPLY).</text>
    </g>

    <text class="cta" x="270" y="1075" font-size="36" text-anchor="middle" textLength="352" lengthAdjust="spacingAndGlyphs">Best For Less Call</text>
    <text class="cta" x="270" y="1130" font-size="44" text-anchor="middle" textLength="460" lengthAdjust="spacingAndGlyphs">Bright Loom Fibers</text>

    <rect class="phone-pill" x="18" y="1161" width="496" height="72" rx="36" fill="#ffffff"/>
    <text class="phone" x="266" y="1218" font-size="56" text-anchor="middle" textLength="410" lengthAdjust="spacingAndGlyphs">866-430-2715</text>
  </svg>

</main>
</body>
</html>
```